Trade Show Banner

Looking for a design for 36" x 90" stretched fabric display.
Commercial construction company, can include Chicago high rise buildings, blue prints, steel studs.
List of types of work should include:
Commercial office build-out
Hospital expansion
Educational and institutional
Laboratory and research
Dental and medical office
Veterinary Clinics

website brolmerconstruction.com

Target Market(s)

Architects and General Contractors

Industry/Entity Type

Commercial Construction

Colors
0054AA
0677BA
7BADD7
CADEEF
E8F1F8

Requirements
Must have
• Our logo, blueprints, chicago high rise
Should not have
• no cartoon construction logos, no houses

```html
<!DOCTYPE html>
<html lang="en">
<head>
<meta charset="utf-8">
<title>Brolmer Construction – Trade Show Banner</title>
<link href="https://fonts.googleapis.com/css2?family=Montserrat:wght@300;500;600;700;800&display=swap" rel="stylesheet">
<style>
  :root {
    --brand-blue: #0054AA;
    --brand-mid: #0677BA;
    --brand-light: #7BADD7;
    --page-bg: #c9c9c9;
    --panel-white: #ffffff;
    --band-grey: #666666;
    --text-dark: #2f2f2f;
    --photo-dark: #1c2230;
    --photo-warm: #6a4a26;
  }
  * { box-sizing: border-box; margin: 0; padding: 0; }
  html, body {
    width: 1200px; height: 1000px; overflow: hidden;
    background: var(--page-bg);
    font-family: "Montserrat", sans-serif;
  }
  .banner {
    position: absolute; left: 414px; top: 35px;
    width: 372px; height: 930px;
    background: var(--panel-white);
    overflow: hidden;
    box-shadow: 0 6px 24px rgba(0,0,0,0.25);
  }
  .hero-photo { position: absolute; left: 0; top: 0; }
  .brand {
    position: absolute; left: 48px; top: 66px;
    display: flex; align-items: center; gap: 12px;
  }
  .brand-square { width: 44px; height: 44px; background: var(--brand-blue); }
  .brand-name {
    color: var(--panel-white); font-weight: 700;
    font-size: 21px; line-height: 23px; letter-spacing: 1.5px;
  }
  .headline {
    position: absolute; left: 66px; top: 190px;
    color: var(--panel-white); font-size: 35px; line-height: 41px;
  }
  .headline .light { font-weight: 300; display: block; }
  .headline .bold { font-weight: 800; display: block; }
  .timeline {
    position: absolute; left: 49px; top: 283px;
    width: 1.5px; height: 210px; background: var(--brand-mid);
  }
  .timeline::after {
    content: ""; position: absolute; left: -2.5px; bottom: -3px;
    width: 6px; height: 6px; border-radius: 50%; background: var(--brand-mid);
  }
  .services {
    position: absolute; left: 49px; top: 469px;
    display: grid; grid-template-columns: 159px 130px; row-gap: 24px;
  }
  .service-head { display: flex; align-items: flex-end; gap: 5px; }
  .service-icon {
    width: 45px; height: 45px; background: var(--brand-blue);
    display: flex; align-items: center; justify-content: center;
  }
  .service-rule { width: 78px; height: 1.5px; background: var(--brand-blue); }
  .service-label {
    margin-top: 10px; color: var(--text-dark);
    font-weight: 500; font-size: 14.5px; line-height: 17px;
  }
  .contact-band {
    position: absolute; left: 0; top: 821px;
    width: 372px; height: 109px; background: var(--band-grey);
  }
  .phone-pill {
    position: absolute; left: 73px; top: 798px;
    width: 262px; height: 45px; border-radius: 23px;
    background: var(--brand-blue);
    color: var(--panel-white); font-weight: 700; font-size: 27px;
    display: flex; align-items: center; padding-left: 26px;
  }
  .phone-badge {
    position: absolute; left: 39px; top: 798px;
    width: 46px; height: 46px; border-radius: 50%;
    background: var(--panel-white); border: 2px solid var(--band-grey);
    display: flex; align-items: center; justify-content: center;
  }
  .website {
    position: absolute; left: 0; top: 854px; width: 372px;
    text-align: center; color: var(--panel-white);
    font-size: 16px; letter-spacing: 2.6px; font-weight: 300;
  }
  .website b { font-weight: 700; }
</style>
</head>
<body>
<main class="banner">
  <svg class="hero-photo" width="372" height="432" viewBox="0 0 372 432" role="img" aria-label="Night photograph of downtown high-rise towers over a lit city street">
    <defs>
      <linearGradient id="photoTone" x1="0" y1="0" x2="0" y2="1">
        <stop offset="0" stop-color="#2a2f3a"/>
        <stop offset="0.55" stop-color="var(--photo-dark)"/>
        <stop offset="0.8" stop-color="var(--photo-warm)"/>
        <stop offset="1" stop-color="#241c16"/>
      </linearGradient>
    </defs>
    <path d="M0 0 H372 V300 C372 380 320 432 230 432 H0 Z" fill="url(#photoTone)"/>
  </svg>

  <div class="brand">
    <div class="brand-square"></div>
    <div class="brand-name">BROLMER<br>CONSTRUCTION</div>
  </div>

  <h1 class="headline">
    <span class="light">part of the</span>
    <span class="light">ever-changing</span>
    <span class="bold">Chicago</span>
    <span class="bold">skyline</span>
  </h1>

  <div class="timeline"></div>

  <section class="services">
    <div class="service">
      <div class="service-head">
        <div class="service-icon"><svg width="30" height="30" viewBox="0 0 30 30" fill="none" stroke="#fff" stroke-width="1.3"><rect x="4" y="8" width="10" height="19"/><rect x="14" y="4" width="8" height="23"/><rect x="22" y="12" width="5" height="15"/><path d="M6 12h6M6 16h6M6 20h6M16 8h4M16 12h4M16 16h4M16 20h4"/></svg></div>
        <div class="service-rule"></div>
      </div>
      <p class="service-label">Commercial<br>office build-out</p>
    </div>
    <div class="service">
      <div class="service-head">
        <div class="service-icon"><svg width="30" height="30" viewBox="0 0 30 30" fill="none" stroke="#fff" stroke-width="1.3"><rect x="5" y="9" width="20" height="18"/><rect x="8" y="3" width="14" height="6" rx="1"/><path d="M9 14h3M14 14h2M18 14h3M9 19h3M18 19h3M13 27v-6h4v6"/></svg></div>
        <div class="service-rule"></div>
      </div>
      <p class="service-label">Laboratory<br>and research</p>
    </div>
    <div class="service">
      <div class="service-head">
        <div class="service-icon"><svg width="30" height="30" viewBox="0 0 30 30" fill="none" stroke="#fff" stroke-width="1.3"><rect x="4" y="12" width="22" height="15"/><rect x="10" y="4" width="10" height="8"/><path d="M15 6v4M13 8h4M7 16h3M20 16h3M7 21h3M20 21h3M13 27v-7h4v7"/></svg></div>
        <div class="service-rule"></div>
      </div>
      <p class="service-label">Hospital<br>expansion</p>
    </div>
    <div class="service">
      <div class="service-head">
        <div class="service-icon"><svg width="30" height="30" viewBox="0 0 30 30" fill="none" stroke="#fff" stroke-width="1.3"><rect x="5" y="10" width="20" height="17"/><path d="M11 4c0 3 1 5 2 5s1-2 2-2 1 2 2 2 2-2 2-5c-2-1-3 0-4 0s-2-1-4 0z"/><path d="M8 14h3M13 14h4M19 14h3M8 19h3M13 19h4M19 19h3M8 24h3M19 24h3"/></svg></div>
        <div class="service-rule"></div>
      </div>
      <p class="service-label">Dental and<br>medical office</p>
    </div>
    <div class="service">
      <div class="service-head">
        <div class="service-icon"><svg width="30" height="30" viewBox="0 0 30 30" fill="none" stroke="#fff" stroke-width="1.3"><rect x="4" y="6" width="22" height="21"/><path d="M4 10h22M8 14h3M13 14h4M19 14h3M8 18h3M19 18h3M12 27v-7h6v7M8 22v5M22 22v5"/></svg></div>
        <div class="service-rule"></div>
      </div>
      <p class="service-label">Educational and<br>institutional</p>
    </div>
    <div class="service">
      <div class="service-head">
        <div class="service-icon"><svg width="30" height="30" viewBox="0 0 30 30" fill="none" stroke="#fff" stroke-width="1.3"><rect x="4" y="4" width="12" height="23"/><rect x="16" y="14" width="10" height="13"/><path d="M7 9h2M7 13h2M7 17h2M7 21h2M21 17v5M18.5 19.5h5M11 8h2"/></svg></div>
        <div class="service-rule"></div>
      </div>
      <p class="service-label">Veterinary<br>Clinics</p>
    </div>
  </section>

  <div class="contact-band"></div>
  <div class="phone-pill">(312) 555-0148</div>
  <div class="phone-badge">
    <svg width="24" height="24" viewBox="0 0 24 24" fill="none" stroke="#555" stroke-width="1.5" stroke-linejoin="round"><path d="M6 3l3 4-2 2c1 3 4 6 7 7l2-2 4 3-2 3C11 20 4 13 3 5z"/><path d="M14 4a6 6 0 0 1 6 6M14 7a3 3 0 0 1 3 3"/></svg>
  </div>
  <p class="website">brolmer<b>construction</b>.com</p>
</main>
</body>
</html>
```